Oil and Gas Company: Letterhead Design

In short we need a professional company letterhead designed for our Oil and Gas company.

We would like to keep the design simple and professional. Letterhead to include the company logo and color scheme, front page and continuation pages.

For reference, see attached logo below with our company logo and color scheme.

Target Market(s)

Oil & Gas Market

Industry/Entity Type

Oil And Gas

Font styles to use
Sans Serif

Requirements
Must have
• Letterhead must contain a front page & continuation page.
• Must be simple and professional in design.
• Follow our logo and color scheme.
Nice to have
• I would like to have the logo embedded in the bottom right hand portion of the page to provide some depth into the letterhead.

```html
<!DOCTYPE html>
<html lang="en">
<head>
<meta charset="utf-8">
<title>Ridgeline Energy Services — Letterhead</title>
<link href="https://fonts.googleapis.com/css2?family=Montserrat:wght@400;500;600&family=Roboto:wght@400;500&display=swap" rel="stylesheet">
<style>
  :root {
    --backdrop: #d3e3e1;
    --paper: #efefef;
    --brand-blue: #0f4192;
    --brand-red: #d0141b;
    --ink: #2a2a2a;
    --ink-soft: #6d6d6d;
    --rule: #b9b9b9;
    --mark-faint: #dcdcdc;
  }
  * { box-sizing: border-box; margin: 0; padding: 0; }
  html, body { width: 1200px; height: 956px; overflow: hidden; }
  body {
    background: var(--backdrop);
    font-family: "Roboto", Arial, sans-serif;
    position: relative;
  }
  .sheet {
    position: absolute;
    top: 124px;
    width: 504px;
    height: 714px;
    background: linear-gradient(160deg, #e6e6e6 0%, var(--paper) 45%, #f3f3f3 100%);
  }
  .sheet--front { left: 54px; }
  .sheet--continuation { left: 646px; }

  .brand {
    position: absolute;
    left: 44px;
    top: 40px;
    width: 92px;
    text-align: center;
    font-family: "Montserrat", Arial, sans-serif;
    font-weight: 500;
    font-size: 8.6px;
    line-height: 10px;
    letter-spacing: 0.3px;
    color: var(--ink);
  }
  .brand__square {
    display: block;
    width: 26px;
    height: 26px;
    margin: 0 auto 14px;
    background: var(--brand-blue);
  }

  .contact {
    position: absolute;
    left: 346px;
    top: 46px;
    padding-left: 18px;
    border-left: 1px solid var(--rule);
    height: 62px;
    font-family: "Montserrat", Arial, sans-serif;
    font-size: 7.6px;
    line-height: 9.4px;
    color: var(--ink);
  }
  .contact__address { padding-top: 10px; margin-bottom: 10px; }
  .contact__line { display: flex; align-items: center; gap: 4px; }
  .contact__line svg { width: 7px; height: 7px; flex: none; }

  .recipient {
    position: absolute;
    left: 45px;
    top: 199px;
    font-size: 9.6px;
    line-height: 11.4px;
    letter-spacing: 0.2px;
    color: var(--ink-soft);
  }
  .recipient__name, .recipient__role { font-weight: 500; color: var(--ink); }

  .letter-date {
    position: absolute;
    right: 44px;
    top: 235px;
    font-size: 9.6px;
    letter-spacing: 0.2px;
    color: var(--ink-soft);
  }

  .letter-body {
    position: absolute;
    left: 46px;
    top: 312px;
    width: 414px;
    font-size: 7.2px;
    line-height: 15.2px;
    letter-spacing: 0.15px;
    color: var(--ink-soft);
    text-align: justify;
  }
  .letter-body p { text-indent: 12px; margin-bottom: 15.2px; }

  .footer-band {
    position: absolute;
    left: 0;
    right: 0;
    top: 673px;
    height: 16px;
  }
  .footer-band__blue {
    position: absolute;
    left: 0;
    top: 0;
    width: 440px;
    height: 16px;
    background: var(--brand-blue);
    clip-path: polygon(0 0, 100% 0, 98.6% 100%, 0 100%);
  }
  .footer-band__red {
    position: absolute;
    right: 0;
    top: 0;
    width: 38px;
    height: 16px;
    background: var(--brand-red);
    clip-path: polygon(4px 0, 100% 0, 100% 100%, 0 100%);
  }
  .footer-band__square {
    position: absolute;
    left: 451px;
    top: -12px;
    width: 12px;
    height: 12px;
    background: var(--mark-faint);
  }
  .footer-band__url {
    position: absolute;
    left: 35px;
    top: 3px;
    font-family: "Montserrat", Arial, sans-serif;
    font-weight: 600;
    font-size: 7.8px;
    letter-spacing: 1.3px;
    color: #ffffff;
  }
</style>
</head>
<body>

<section class="sheet sheet--front" aria-label="Front page">
  <div class="brand">
    <span class="brand__square"></span>
    RIDGELINE<br>ENERGY SERVICES
  </div>

  <div class="contact">
    <div class="contact__address">418 N Mill Avenue<br>Laurel, MS 39440</div>
    <div class="contact__line">
      <svg viewBox="0 0 10 10" aria-hidden="true"><path d="M2 1 L4 1 L4.8 3.2 L3.6 4.2 Q4.6 6 6 6.6 L7 5.4 L9 6.2 L9 8.2 Q5 9 2.6 6 Q1 3.8 2 1 Z" fill="var(--brand-red)"/></svg>
      000 000 0000
    </div>
    <div class="contact__line">
      <svg viewBox="0 0 10 10" aria-hidden="true"><rect x="0.8" y="2" width="8.4" height="6" fill="none" stroke="var(--brand-red)" stroke-width="1"/><path d="M0.8 2 L5 5.4 L9.2 2" fill="none" stroke="var(--brand-red)" stroke-width="1"/></svg>
      info@yourwebsite.com
    </div>
  </div>

  <div class="recipient">
    <div class="recipient__name">MR. Daniel HARTLEY</div>
    <div class="recipient__role">Managing Director</div>
    <div>12/7 Harbor Court</div>
    <div>Oregon - 987654321</div>
  </div>

  <div class="letter-date">Date : 01 July 2018</div>

  <div class="letter-body">
    <p>Lorem ipsum dolor sit amet, justo platonem in per, dicant constituto ne eam. Aeque persecuti sit ea, at vis commodo tractatos vituperata, sea an albucius forensibus. Wisi quodsi id qui, duo tempor aliquam assentior eu, no diceret tibique definiebas mei. Id nec noster facilisi mandamus.</p>
    <p>Nullam definiebas signiferumque pro te, vel mutat lobortis conceptam in. Usu justo minimum an, ne regione sanctus praesent usu, eam ut adipisci volutpat. Vel odio tibique consequat ne, in dicit gubergren appellantur vis, quo ei omnis elitr. Qui ne enim dictas dissentiet, pro nulla quodsi deseruisse te. Vide prima eloquentiam pro ei, agam dicta in pro, eu persius propriae constituam sea. Ius ut iriure oblique laboramus, cu sed fugit commune invenire, viris repudiandae ex vis. Nullam definiebas signiferumque pro te, vel mutat lobortis conceptam in. Usu justo minimum an, ne regione sanctus praesent usu, eam ut adipisci volutpat. Vel odio tibique consequat ne, in dicit gubergren appellantur vis, quo ei omnis elitr. Qui ne enim dictas dissentiet, pro nulla quodsi deseruisse te. Vide prima eloquentiam pro ei, agam dicta in pro, eu persius propriae constituam sea. Ius ut iriure oblique laboramus, cu sed fugit commun.</p>
  </div>

  <div class="footer-band">
    <div class="footer-band__blue"></div>
    <span class="footer-band__square"></span>
    <div class="footer-band__red"></div>
    <span class="footer-band__url">www.yourwebsite.com</span>
  </div>
</section>

<section class="sheet sheet--continuation" aria-label="Continuation page">
  <div class="footer-band">
    <div class="footer-band__blue"></div>
    <span class="footer-band__square"></span>
    <div class="footer-band__red"></div>
    <span class="footer-band__url">www.yourwebsite.com</span>
  </div>
</section>

</body>
</html>
```